Business Card for New Convenience Store

We need a business card for our new convenience store using our logo. We want to have a color scheme and back ground created that will be transferable to other media platforms and advertising.

Industry/Entity Type

Convenience Store

```html
<!DOCTYPE html>
<html lang="en">
<head>
<meta charset="utf-8">
<title>ODS Harlow — Business Card</title>
<link rel="stylesheet" href="https://fonts.googleapis.com/css2?family=Questrial&display=swap">
<style>
  :root {
    --page: #ece7df;
    --taupe: #a99b86;
    --olive-dark: #6b5a36;
    --olive-light: #a9993f;
    --brown-deep: #4a3a1c;
    --text-light: #b8ab7c;
    --text-pale: #c9bd9a;
    --frame: #5e4838;
    --sky: #cfd7e0;
    --wall: #7d6450;
    --white: #ffffff;
  }
  * { margin: 0; padding: 0; box-sizing: border-box; }
  html, body { width: 1200px; height: 1000px; overflow: hidden; }
  body {
    background: var(--page);
    font-family: "Questrial", sans-serif;
    position: relative;
  }
  .card {
    position: absolute;
    left: 188px;
    width: 822px;
    height: 446px;
    overflow: hidden;
    box-shadow: 0 3px 8px rgba(0,0,0,0.25);
  }
  .card--front { top: 36px; }
  .card--back { top: 516px; background: var(--frame); }

  .bands { position: absolute; inset: 0; }

  .slant {
    position: absolute;
    white-space: nowrap;
    line-height: 1;
    transform-origin: 0 100%;
    transform: rotate(-57deg);
  }
  .brand-name { color: var(--brown-deep); font-size: 92px; letter-spacing: -2px; }
  .brand-place { color: var(--brown-deep); font-size: 92px; letter-spacing: -2px; }
  .person-name { color: var(--text-light); font-size: 52px; }
  .person-role { color: var(--text-light); font-size: 38px; }
  .contact { color: var(--brown-deep); font-size: 40px; }
  .address { color: var(--text-pale); font-size: 37px; }

  .storefront {
    position: absolute;
    left: 34px; top: 34px;
    width: 754px; height: 382px;
    border-radius: 16px;
    background: linear-gradient(180deg, var(--sky) 0%, #b9c2c6 28%, var(--wall) 55%, #8a7868 80%, #dcdcd8 100%);
    box-shadow: inset 0 0 10px rgba(0,0,0,0.35);
  }
  .storefront-brand {
    position: absolute;
    left: 540px; top: 108px;
    color: var(--white);
    font-size: 40px;
    line-height: 1;
    letter-spacing: 1px;
  }
  .storefront-brand span { display: block; font-size: 26px; margin-left: 44px; margin-top: 4px; }
</style>
</head>
<body>

  <section class="card card--front" aria-label="Business card front">
    <svg class="bands" width="822" height="446" viewBox="0 0 822 446" aria-hidden="true">
      <rect width="822" height="446" fill="var(--taupe)"/>
      <polygon points="402,0 822,0 822,446 137,446" fill="var(--olive-dark)"/>
      <polygon points="587,0 747,0 477,446 317,446" fill="var(--olive-light)"/>
    </svg>

    <div class="slant brand-name" style="left:60px; top:222px;">ODS</div>
    <div class="slant brand-place" style="left:138px; top:264px; font-size:46px;">HARLOW</div>

    <div class="slant person-name" style="left:252px; top:297px;">Dana Whitfield</div>
    <div class="slant person-role" style="left:348px; top:286px;">Manager</div>

    <div class="slant contact" style="left:442px; top:279px;">555-014-2738</div>
    <div class="slant contact" style="left:466px; top:364px;">dwhitfield@odsmail.com</div>

    <div class="slant address" style="left:560px; top:382px;">12 Cedar Bend Rd.</div>
    <div class="slant address" style="left:628px; top:346px;">Harlow</div>
    <div class="slant address" style="left:692px; top:367px;">AL 35999</div>
  </section>

  <section class="card card--back" aria-label="Business card back">
    <div class="storefront" role="img" aria-label="Rendering of the store exterior with stone walls, large glass front and shoppers walking in"></div>
    <div class="storefront-brand">ODS<span>HARLOW</span></div>
  </section>

</body>
</html>
```